Business card for psychiatrist

Business card design project for a psychiatristWe would like to have the impression of 1. We (patient and the doctor) are working together.2. Light the way so that patients can see where they are going and what their goals are.3. One side of the business card will have the letter "BFP" which stands for Brynmoor Family Psychiatry.4. The other side of the business card will have the address, phone number, name of the psychiatrist, website, etc.5. A logo could go into either side of the business card. Let's see what looks better.
Business card design project for a psychiatrist
We would like to have the impression of
1. We (patient and the doctor) are working together.
2. Light the way so that patients can see where they are going and what their goals are.
3. One side of the business card will have the letter "BFP" which stands for Brynmoor Family Psychiatry.
4. The other side of the business card will have the address, phone number, name of the psychiatrist, website, etc.
5. A logo could go into either side of the business card. Let's see what looks better.

```html
<!DOCTYPE html>
<html lang="en">
<head>
<meta charset="utf-8">
<title>Brynmoor Family Psychiatry – Business Card</title>
<link href="https://fonts.googleapis.com/css2?family=Arimo:wght@400;700&display=swap" rel="stylesheet">
<style>
  :root {
    --backdrop: #cecece;
    --card-white: #ffffff;
    --brand-green: #8cc043;
    --brand-blue: #2ea3db;
    --ink: #1c1c1c;
  }
  * { box-sizing: border-box; margin: 0; padding: 0; }
  html, body {
    width: 1200px; height: 900px; overflow: hidden;
    background: var(--backdrop);
    font-family: "Arimo", Arial, sans-serif;
  }
  .card {
    position: absolute;
    width: 652px; height: 372px;
    overflow: hidden;
  }
  /* Front side */
  .card--front { left: 274px; top: 57px; background: var(--card-white); }
  .card__swoosh { position: absolute; inset: 0; }
  .accent-bar {
    position: absolute; left: 0; top: 57px;
    width: 12px; height: 41px; background: var(--brand-green);
  }
  .person__name {
    position: absolute; left: 33px; top: 50px;
    font-size: 34px; font-weight: 400; color: var(--brand-green);
    letter-spacing: 0.2px;
  }
  .person__role {
    position: absolute; left: 34px; top: 85px;
    font-size: 15.5px; color: var(--ink);
  }
  .divider {
    position: absolute; left: 33px; top: 160px;
    width: 31px; height: 3px; background: var(--brand-green);
  }
  .address {
    position: absolute; left: 33px; top: 174px;
    font-size: 14.5px; line-height: 18px; color: var(--ink);
    font-style: normal;
  }
  .contact-list { list-style: none; position: absolute; left: 33px; top: 219px; }
  .contact-list li {
    display: flex; align-items: center;
    height: 25.5px; font-size: 14.5px; color: var(--ink);
  }
  .contact-list svg { width: 17px; height: 17px; margin-right: 9px; flex: none; }
  .brand-mark {
    position: absolute; left: 480px; top: 72px;
    display: flex; align-items: center; gap: 10px;
  }
  .brand-mark__dot {
    width: 34px; height: 34px; border-radius: 50%; background: var(--brand-blue);
  }
  .brand-mark__name {
    font-size: 46px; font-weight: 700; color: var(--brand-green); line-height: 1;
  }

  /* Back side */
  .card--back { left: 278px; top: 483px; background: var(--brand-green); }
  .back-mark {
    position: absolute; left: 0; right: 0; top: 125px;
    display: flex; justify-content: center; align-items: center; gap: 16px;
  }
  .back-mark__dot {
    width: 54px; height: 54px; border-radius: 50%; background: var(--card-white);
  }
  .back-mark__name {
    font-size: 92px; font-weight: 700; color: var(--card-white); line-height: 1;
  }
  .name-band {
    position: absolute; left: 0; right: 0; top: 311px; height: 40px;
    background: var(--brand-blue);
    display: flex; align-items: center; justify-content: center;
    color: var(--card-white); font-size: 27px;
  }
</style>
</head>
<body>

<section class="card card--front" aria-label="Business card front">
  <svg class="card__swoosh" viewBox="0 0 652 372" width="652" height="372" aria-hidden="true">
    <path d="M0 344 Q420 358 652 203 L652 372 L0 372 Z" fill="var(--brand-green)"/>
    <path d="M0 337 Q420 350 652 196" fill="none" stroke="var(--brand-blue)" stroke-width="8"/>
  </svg>

  <div class="accent-bar"></div>
  <h1 class="person__name">Marisa Van Heerden</h1>
  <p class="person__role">Director</p>
  <div class="divider"></div>

  <address class="address">
    Unit 12, Larkspur Court, Willowmere<br>
    St, Ashdene AH, Fairhaven, 1742
  </address>

  <ul class="contact-list">
    <li>
      <svg viewBox="0 0 24 24" aria-hidden="true"><path d="M6.6 10.8a15 15 0 0 0 6.6 6.6l2.2-2.2c.3-.3.7-.4 1-.2 1.1.4 2.3.6 3.6.6.6 0 1 .4 1 1V20c0 .6-.4 1-1 1A17 17 0 0 1 3 4c0-.6.4-1 1-1h3.5c.6 0 1 .4 1 1 0 1.3.2 2.5.6 3.6.1.3 0 .7-.2 1z" fill="var(--brand-green)"/></svg>
      010 555 0142
    </li>
    <li>
      <svg viewBox="0 0 24 24" aria-hidden="true"><path d="M6.6 10.8a15 15 0 0 0 6.6 6.6l2.2-2.2c.3-.3.7-.4 1-.2 1.1.4 2.3.6 3.6.6.6 0 1 .4 1 1V20c0 .6-.4 1-1 1A17 17 0 0 1 3 4c0-.6.4-1 1-1h3.5c.6 0 1 .4 1 1 0 1.3.2 2.5.6 3.6.1.3 0 .7-.2 1z" fill="var(--brand-green)"/></svg>
      076 555 0198
    </li>
    <li>
      <svg viewBox="0 0 24 24" aria-hidden="true"><rect x="2" y="5" width="20" height="14" fill="var(--brand-green)"/><path d="M2 5l10 8 10-8M2 19l7.5-7M22 19l-7.5-7" fill="none" stroke="#fff" stroke-width="1.6"/></svg>
      marisa@brynmoorfamily.org.za
    </li>
    <li>
      <svg viewBox="0 0 24 24" aria-hidden="true"><circle cx="12" cy="12" r="10" fill="none" stroke="var(--brand-green)" stroke-width="2"/><path d="M12 2v20M2 12h20M12 2c-4 3-4 17 0 20M12 2c4 3 4 17 0 20" fill="none" stroke="var(--brand-green)" stroke-width="1.4"/></svg>
      www.brynmoorfamily.org.za
    </li>
  </ul>

  <div class="brand-mark">
    <span class="brand-mark__dot"></span>
    <span class="brand-mark__name">BFP</span>
  </div>
</section>

<section class="card card--back" aria-label="Business card back">
  <div class="back-mark">
    <span class="back-mark__dot"></span>
    <span class="back-mark__name">BFP</span>
  </div>
  <div class="name-band">Brynmoor Family Psychiatry</div>
</section>

</body>
</html>
```